Harbor Crest Fleet Service Buisness card

We need to create a business card with the same theme you came up with for the truck. I have attached a picture of the truck for you to see. Also there is a picture of the logo as well as a sample business card that I really don't like.

Target Market(s)

Fleet service and heave equipment work

Industry/Entity Type

Fleet Service

Contact Information for Business Card

I have attached a sample card I want to make better. It has basic details on it.

Colors
0054AA
0677BA
7BADD7
CADEEF
E8F1F8
F0912C
F2A743
F7CA91
FBE8D2
FDF5EE

Requirements
Must have
• "Professional and clean, and I want to list some basic services. They include, "Mobile Hydraulics", Fleet Service, Computer diagnostics, "Roadside Service". I also want it to say "We come to you" and 24/7"
Nice to have
• Our Phone number is 1-888-512-7694

```html
<!DOCTYPE html>
<html lang="en">
<head>
<meta charset="utf-8">
<title>Harbor Crest Fleet Service – Business Card</title>
<link rel="stylesheet" href="https://fonts.googleapis.com/css2?family=Montserrat:wght@600;700;800&family=Roboto:wght@400;500&display=swap">
<style>
  :root {
    --navy: #0a3a6b;
    --navy-deep: #072c53;
    --blue: #0054aa;
    --orange: #f2a743;
    --orange-soft: #f0b867;
    --paper: #f6f6f4;
    --ink: #1e2b3a;
    --grey: #6f7378;
    --stage: #e9ebee;
  }
  * { box-sizing: border-box; margin: 0; padding: 0; }
  html, body { width: 1200px; height: 1050px; overflow: hidden; }
  body {
    background: var(--stage);
    font-family: "Roboto", Arial, sans-serif;
    position: relative;
  }
  .card {
    position: absolute;
    width: 600px;
    height: 345px;
    border-radius: 26px;
    overflow: hidden;
    box-shadow: 0 6px 18px rgba(0,0,0,.12);
  }

  /* Front */
  .card-front {
    left: 300px; top: 130px;
    background: var(--navy);
  }
  .card-front .brand {
    position: absolute; left: 0; right: 0; top: 78px;
    text-align: center;
    font-family: "Montserrat", Arial, sans-serif;
    font-weight: 800;
    color: #ffffff;
    font-size: 40px;
    line-height: 1.05;
    letter-spacing: 1px;
  }
  .card-front .tagline {
    position: absolute; left: 0; right: 0; top: 178px;
    text-align: center;
    font-family: "Montserrat", Arial, sans-serif;
    font-weight: 700;
    font-size: 24px;
    color: var(--orange);
  }
  .card-front .services-pill {
    position: absolute; left: 50%; top: 222px;
    transform: translateX(-50%);
    border: 2px solid var(--orange);
    border-radius: 10px;
    padding: 5px 22px;
    font-family: "Montserrat", Arial, sans-serif;
    font-weight: 700;
    font-size: 17px;
    color: #ffffff;
    letter-spacing: 1px;
  }
  .card-front .service-band {
    position: absolute; left: 0; right: 0; bottom: 0;
    height: 50px;
    background: var(--orange-soft);
    display: flex; align-items: center; justify-content: center;
    font-size: 15px;
    font-weight: 500;
    color: var(--navy-deep);
  }

  /* Back */
  .card-back {
    left: 300px; top: 530px;
    background: var(--paper);
  }
  .card-back .edge-tab {
    position: absolute; left: -34px; top: 96px;
    width: 58px; height: 58px; border-radius: 50%;
    background: var(--navy);
  }
  .card-back .person {
    position: absolute; left: 48px; top: 98px;
  }
  .card-back .person-name {
    font-family: "Montserrat", Arial, sans-serif;
    font-weight: 800;
    font-size: 22px;
    color: var(--navy);
    letter-spacing: .5px;
  }
  .card-back .person-role {
    font-size: 15px; color: var(--ink); margin-top: 2px;
  }
  .card-back .address {
    position: absolute; left: 48px; top: 192px;
    font-size: 15px; color: var(--ink); line-height: 1.35;
  }
  .card-back .contact-list {
    position: absolute; left: 48px; top: 242px;
    list-style: none;
  }
  .card-back .contact-list li {
    display: flex; align-items: center; gap: 10px;
    font-size: 15px; color: var(--ink); line-height: 1.6;
  }
  .card-back .contact-list svg { width: 14px; height: 14px; flex: none; }
  .card-back .hours {
    position: absolute; right: 40px; top: 32px;
    display: flex; align-items: center; gap: 4px;
    color: var(--blue);
    font-family: "Montserrat", Arial, sans-serif;
    font-weight: 800;
  }
  .card-back .hours-num { font-size: 26px; line-height: 1; }
  .card-back .hours-label { font-size: 9px; display: block; letter-spacing: .5px; }
  .card-back .brand {
    position: absolute; right: 46px; top: 150px;
    width: 220px;
    text-align: center;
    font-family: "Montserrat", Arial, sans-serif;
    font-weight: 800;
    font-size: 26px;
    line-height: 1.1;
    color: var(--navy);
  }
</style>
</head>
<body>

<section class="card card-front" aria-label="Business card front">
  <div class="brand">HARBOR CREST<br>FLEET SERVICE</div>
  <div class="tagline">We come to you...</div>
  <div class="services-pill">OUR SERVICES</div>
  <div class="service-band">Mobile Hydraulics | Fleet Service | Computer diagnostics | Roadside Service</div>
</section>

<section class="card card-back" aria-label="Business card back">
  <div class="edge-tab"></div>

  <div class="hours">
    <svg width="30" height="30" viewBox="0 0 30 30" aria-hidden="true">
      <path d="M15 3 A12 12 0 1 0 27 15" fill="none" stroke="currentColor" stroke-width="2.5"/>
      <path d="M15 8 V15 H21" fill="none" stroke="currentColor" stroke-width="2.5"/>
    </svg>
    <div><span class="hours-num">24</span><span class="hours-label">HOURS</span></div>
  </div>

  <div class="person">
    <div class="person-name">DANIEL WHITFORD</div>
    <div class="person-role">Managing Director</div>
  </div>

  <div class="address">4120, Mill Creek Rd.<br>Lakeview FL 33810</div>

  <ul class="contact-list">
    <li>
      <svg viewBox="0 0 16 16" aria-hidden="true"><circle cx="8" cy="8" r="7" fill="none" stroke="#0a3a6b" stroke-width="1.5"/><path d="M5.5 4.5l1.5 1.5-1 1c.6 1.3 1.5 2.2 2.8 2.8l1-1 1.5 1.5-1 1.2C7.6 11.3 4.7 8.4 4.5 5.5z" fill="#0a3a6b"/></svg>
      1-888-512-7694
    </li>
    <li>
      <svg viewBox="0 0 16 16" aria-hidden="true"><rect x="1.5" y="3.5" width="13" height="9" fill="none" stroke="#0a3a6b" stroke-width="1.5"/><path d="M1.5 3.5L8 9l6.5-5.5" fill="none" stroke="#0a3a6b" stroke-width="1.5"/></svg>
      daniel@harborcrestfleet.com
    </li>
    <li>
      <svg viewBox="0 0 16 16" aria-hidden="true"><circle cx="8" cy="8" r="6.5" fill="none" stroke="#0a3a6b" stroke-width="1.5"/><path d="M1.5 8h13M8 1.5c-3 3.5-3 9.5 0 13M8 1.5c3 3.5 3 9.5 0 13" fill="none" stroke="#0a3a6b" stroke-width="1.2"/></svg>
      www.harborcrestfleet.com
    </li>
  </ul>

  <div class="brand">HARBOR CREST<br>FLEET SERVICE</div>
</section>

</body>
</html>
```